Group training gym/bootcamp needs a web design

We need a website for our gym that is based in Sydney. We have indoor functional training classes and outdoor bootcamp classes. We would like the web site to have a video (to be created) and photo gallery. I would like the site made on word press and i would like to be able to make minor changes such as changing images and text without having to use a designer.

The website should have the following pages: home page; the gym; the bootcamp; photo gallery; about us; contact.

I have uploaded our logo and i would like to keep to these colour (blue,yellow,silver) and black is also allowed

Target Market(s)

18-50 male and female

Industry/Entity Type

Gym

Coding

Coded - Design and coding required

Number of Pages Required

5+ page

Font styles to use
Sans Serif

Colors
0692cd
fbed22
1b1b1b
e8e8e8

Requirements
Must have
• The website should have the following pages: home page; the gym; the bootcamp; photo gallery; about us; contact.
• I have uploaded our logo and i would like to keep to these colour (blue,yellow,silver) and black is also allowed
• Video upload and photo upload

```html
<!DOCTYPE html>
<html lang="en">
<head>
<meta charset="utf-8">
<title>Ironside Training Hub</title>
<link href="https://fonts.googleapis.com/css2?family=Jost:wght@400;500;600;700&family=Lato:wght@400;700&display=swap" rel="stylesheet">
<style>
:root{
  --gold:#e6b712;
  --gold-light:#f2cd3a;
  --blue:#1a6fb5;
  --ink:#1b1b1b;
  --dark:#2d2d2d;
  --footer:#333333;
  --silver:#e8e8e8;
  --text:#555555;
  --white:#ffffff;
}
*{margin:0;padding:0;box-sizing:border-box}
html,body{width:1200px;height:2744px;overflow:hidden}
body{position:relative;font-family:"Lato",sans-serif;color:var(--ink);background:var(--white)}
.abs{position:absolute}

/* top bar */
.topbar{left:0;top:0;width:1200px;height:31px;background:var(--dark);color:var(--white);font-size:13px}
.topbar .item{position:absolute;top:8px;display:flex;align-items:center;gap:8px}
.header{left:0;top:31px;width:1200px;height:79px;background:var(--white)}
.brand{left:161px;top:22px;display:flex;align-items:center;gap:10px;font-family:"Jost",sans-serif;font-weight:700;font-size:22px;color:var(--blue);letter-spacing:.5px}
.brand .mark{width:16px;height:16px;background:var(--gold);border-radius:50%}
.nav a{position:absolute;top:32px;font-size:15px;color:var(--ink);text-decoration:none}
.nav a.active{color:var(--blue)}

/* hero */
.hero{left:0;top:110px;width:1200px;height:525px;background:radial-gradient(ellipse at 50% 45%,#6a4a33 0%,#3a2a20 35%,#141414 75%)}
.hero h1{position:absolute;left:0;width:1200px;top:330px;text-align:center;font-family:"Jost",sans-serif;font-weight:600;font-size:50px;color:var(--gold);letter-spacing:.5px}
.hero .lead{position:absolute;left:0;width:1200px;top:383px;text-align:center;font-size:30px;color:var(--white)}
.btn{display:inline-block;background:var(--gold);color:var(--ink);border-radius:8px;text-align:center;font-family:"Lato",sans-serif}
.hero .btn{position:absolute;left:494px;top:459px;width:212px;height:53px;line-height:53px;font-size:28px;background:linear-gradient(#f5d241,#e2b10e)}
.dot{position:absolute;top:576px;width:18px;height:18px;border-radius:50%;background:var(--white)}
.dot.on{background:var(--gold)}

/* about */
.about-left{left:0;top:635px;width:598px;height:387px;background:var(--gold)}
.about-photo{left:100px;top:670px;width:385px;height:320px;background:radial-gradient(ellipse at 50% 55%,#5d6f86 0%,#c09a1a 60%,rgba(230,183,18,0) 72%)}
.about-title{right:636px;top:756px;text-align:right;font-family:"Jost",sans-serif;color:var(--white);font-size:37px;line-height:46px}
.about-title b{font-weight:700}
.notch{left:598px;top:816px;width:0;height:0;border-top:14px solid transparent;border-bottom:14px solid transparent;border-left:12px solid var(--gold)}
.feature{left:649px;width:440px}
.feature h3{display:flex;align-items:center;gap:14px;font-family:"Lato",sans-serif;font-weight:700;font-size:16px;color:var(--ink);margin-bottom:10px}
.feature p{padding-left:35px;font-size:12px;line-height:19px;color:var(--text)}
.feature p span{color:var(--gold)}

/* section heads */
.section-title{left:0;width:1200px;text-align:center;font-family:"Jost",sans-serif;font-weight:600;font-size:40px;color:var(--ink)}
.section-title span{color:var(--blue)}
.divider{left:520px;width:160px;height:14px}

/* services */
.services{left:0;top:1022px;width:1200px;height:688px;background:radial-gradient(ellipse at 50% 40%,#eef0ec 0%,#e3e6e0 60%,#d9ddd6 100%)}
.tab{top:1179px;font-family:"Jost",sans-serif;font-size:17px;color:#777}
.tab.active{color:var(--ink);font-weight:500;border-bottom:3px solid var(--gold);padding-bottom:4px}
.service-photo{left:596px;top:1240px;width:443px;height:410px;background:linear-gradient(180deg,#5f7d4a 0%,#4f7a3a 45%,#3f6c2d 100%)}
.service-card{left:161px;top:1256px;width:481px;height:372px;background:var(--white);box-shadow:0 8px 22px rgba(0,0,0,.22);padding:52px 36px 0 36px}
.service-card h4{font-family:"Lato",sans-serif;font-weight:700;font-size:17px;color:var(--blue);margin-bottom:17px}
.service-card h5{font-size:14px;font-weight:700;color:var(--ink);margin-bottom:14px}
.service-card p{font-size:11.5px;line-height:19.5px;color:var(--text)}
.service-card .btn{position:absolute;left:35px;top:302px;width:104px;height:26px;line-height:26px;font-size:13px;border-radius:5px}

/* gallery */
.tile{background:linear-gradient(135deg,#6e8f55,#3f5f30)}
.tile.gym{background:linear-gradient(135deg,#6b6f75,#2e3136)}

/* footer */
.footer{left:0;top:2433px;width:1200px;height:270px;background:var(--footer);color:var(--white)}
.footer h6{position:absolute;top:35px;font-family:"Jost",sans-serif;font-weight:500;font-size:17px;padding-bottom:10px;border-bottom:1px solid #5a5a5a}
.footer h6 span{color:var(--gold)}
.footer .links a{position:absolute;left:161px;font-size:11.5px;color:var(--white);text-decoration:none}
.footer .links a.active{font-weight:700}
.footer .info{position:absolute;left:311px;font-size:11.5px;line-height:14px}
.field{position:absolute;left:569px;width:207px;background:var(--white);border-radius:3px;font-size:10px;color:#999;padding:5px 7px}
.footer .btn{position:absolute;left:569px;top:212px;width:106px;height:24px;line-height:24px;font-size:13px;border-radius:4px}
.footer-brand{left:832px;top:2520px;width:210px;display:flex;align-items:center;gap:8px;font-family:"Jost",sans-serif;font-weight:600;font-size:19px;color:var(--silver)}
.footer-brand .mark{width:14px;height:14px;border-radius:50%;background:var(--silver)}
.copyright{left:0;top:2703px;width:1200px;height:41px;background:var(--gold);text-align:center;line-height:41px;font-size:12px;color:var(--ink)}
</style>
</head>
<body>

<div class="abs topbar">
  <div class="item" style="left:706px">
    <svg width="13" height="13" viewBox="0 0 24 24"><path fill="#e6b712" d="M6.6 10.8a15.1 15.1 0 0 0 6.6 6.6l2.2-2.2c.3-.3.7-.4 1-.2 1.1.4 2.3.6 3.6.6.6 0 1 .4 1 1V20c0 .6-.4 1-1 1A17 17 0 0 1 3 4c0-.6.4-1 1-1h3.5c.6 0 1 .4 1 1 0 1.3.2 2.5.6 3.6.1.3 0 .7-.2 1z"/></svg>
    <span>123 456 7890</span>
  </div>
  <div class="item" style="left:826px">
    <svg width="14" height="11" viewBox="0 0 24 18"><rect width="24" height="18" rx="2" fill="#e6b712"/><path d="M1 2l11 8 11-8" stroke="#2d2d2d" stroke-width="2" fill="none"/></svg>
    <span>info@ironsidetraininghub.com</span>
  </div>
</div>

<header class="abs header">
  <div class="abs brand"><span class="mark"></span>Ironside Training Hub</div>
  <nav class="nav">
    <a class="active" href="#" style="left:446px">Home</a>
    <a href="#" style="left:535px">About Us</a>
    <a href="#" style="left:644px">The Gym</a>
    <a href="#" style="left:751px">The Bootcamp</a>
    <a href="#" style="left:891px">Gallery</a>
    <a href="#" style="left:989px">Contact</a>
  </nav>
</header>

<section class="abs hero" role="img" aria-label="Dark gym photo of an athlete seen from behind, arms raised">
  <h1>IRONSIDE TRAINING HUB</h1>
  <p class="lead">Lorem ipsum dolor sit amet, consectetuer adipiscing elit</p>
  <a class="btn" href="#">Join With Us</a>
  <span class="dot" style="left:554px"></span>
  <span class="dot on" style="left:580px"></span>
  <span class="dot" style="left:604px"></span>
  <span class="dot" style="left:626px"></span>
</section>

<section>
  <div class="abs about-left"></div>
  <div class="abs about-photo" role="img" aria-label="Woman in sportswear doing a deep side lunge stretch"></div>
  <h2 class="abs about-title">All About<br><b>FITNESS</b></h2>
  <div class="abs notch"></div>

  <div class="abs feature" style="top:685px">
    <h3><svg width="21" height="12" viewBox="0 0 21 12"><rect x="0" y="2" width="4" height="8" fill="#e6b712"/><rect x="17" y="2" width="4" height="8" fill="#e6b712"/><rect x="4" y="5" width="13" height="2" fill="#e6b712"/></svg>Weight Lifting</h3>
    <p>Lorem ipsum dolor sit elit amet, consectetuer adipiscing elit, sed diam nonummy nibh euismod tincidunt ut laoreet dolore...<span>[+]</span></p>
  </div>
  <div class="abs feature" style="top:795px">
    <h3><svg width="21" height="18" viewBox="0 0 21 18"><circle cx="13" cy="3" r="2.5" fill="#e6b712"/><path d="M11 6l-4 4 3 2-2 6M11 6l3 5 4 0M9 9l-5 1" stroke="#e6b712" stroke-width="2.2" fill="none" stroke-linecap="round"/></svg>Running</h3>
    <p>Lorem ipsum dolor sit elit amet, consectetuer adipiscing elit, sed diam nonummy nibh euismod tincidunt ut laoreet dolore...<span>[+]</span></p>
  </div>
  <div class="abs feature" style="top:903px">
    <h3><svg width="21" height="18" viewBox="0 0 21 18"><circle cx="10.5" cy="3.5" r="3" fill="#e6b712"/><path d="M4 17c0-6 3-9 6.5-9S17 11 17 17z" fill="#e6b712"/></svg>Yoga</h3>
    <p>Lorem ipsum dolor sit elit amet, consectetuer adipiscing elit, sed diam nonummy nibh euismod tincidunt ut laoreet dolore...<span>[+]</span></p>
  </div>
</section>

<section>
  <div class="abs services" role="img" aria-label="Faded outdoor bootcamp class background"></div>
  <h2 class="abs section-title" style="top:1070px">OUR <span>SERVICES</span></h2>
  <svg class="abs divider" style="top:1126px" viewBox="0 0 160 14"><line x1="0" y1="9" x2="160" y2="9" stroke="#aaa"/><circle cx="80" cy="7" r="5" fill="#999"/></svg>
  <span class="abs tab" style="left:161px">The Gym</span>
  <span class="abs tab active" style="left:247px">The Boot Camp</span>

  <div class="abs service-photo" role="img" aria-label="Outdoor bootcamp group exercising on grass with arms raised"></div>
  <article class="abs service-card">
    <h4>The Boot Camp</h4>
    <h5>sed diam nonummy nibh euismod tincidunt ut laoreet</h5>
    <p>Lorem ipsum dolor sit amet, consectetuer adipiscing elit, sed diam nonummy nibh euismod tincidunt ut laoreet dolore magna aliquam erat volutpat. Ut wisi enim ad minim veniam, quis nostrud exerci tation ullamcorper suscipit lobortis nisl ut aliquip ex ea commodo consequat. Duis autem vel eum iriure dolor in hendrerit in vulputate velit esse molestie consequat, vel illum dolore eu feugiat nulla facilisis at vero eros et accumsan et iusto odio dignissim qui blandit praesent luptatum zzril delenit augue duis dolore te feugait nulla facilisi.</p>
    <a class="btn" href="#">Read More</a>
  </article>
</section>

<section>
  <h2 class="abs section-title" style="top:1758px">OUR <span>GALLERY</span></h2>
  <svg class="abs divider" style="top:1814px" viewBox="0 0 160 14"><line x1="0" y1="9" x2="160" y2="9" stroke="#aaa"/><circle cx="80" cy="7" r="5" fill="#999"/></svg>
  <div class="abs tile" style="left:161px;top:1862px;width:430px;height:247px" role="img" aria-label="Group doing push-ups on grass outdoors"></div>
  <div class="abs tile" style="left:609px;top:1862px;width:207px;height:247px" role="img" aria-label="Women doing dumbbell step exercises outdoors"></div>
  <div class="abs tile" style="left:832px;top:1862px;width:207px;height:247px" role="img" aria-label="Outdoor group class jumping on paved park"></div>
  <div class="abs tile gym" style="left:161px;top:2125px;width:207px;height:247px" role="img" aria-label="Man pressing dumbbells on a bench"></div>
  <div class="abs tile gym" style="left:384px;top:2125px;width:207px;height:247px" role="img" aria-label="Woman training on a gym machine"></div>
  <div class="abs tile gym" style="left:609px;top:2125px;width:430px;height:247px" role="img" aria-label="People running on treadmills in a gym"></div>
</section>

<footer class="abs footer">
  <h6 style="left:161px;width:95px">Quick <span>Link</span></h6>
  <div class="links">
    <a class="active" href="#" style="top:84px">Home</a>
    <a href="#" style="top:113px">About</a>
    <a href="#" style="top:142px">The Gym</a>
    <a href="#" style="top:171px">The Bootcamp</a>
    <a href="#" style="top:200px">Gallery</a>
    <a href="#" style="top:229px">Contact</a>
  </div>

  <h6 style="left:311px;width:95px">Contact <span>Info</span></h6>
  <div class="info" style="top:84px"><b>Ironside Training Hub</b><br>Lorem ipsum dolor sit amet,<br>consectetuer adipiscing elit<br>1234</div>
  <div class="info" style="top:177px;display:flex;gap:8px;align-items:center">
    <svg width="12" height="12" viewBox="0 0 24 24"><path fill="#fff" d="M6.6 10.8a15.1 15.1 0 0 0 6.6 6.6l2.2-2.2c.3-.3.7-.4 1-.2 1.1.4 2.3.6 3.6.6.6 0 1 .4 1 1V20c0 .6-.4 1-1 1A17 17 0 0 1 3 4c0-.6.4-1 1-1h3.5c.6 0 1 .4 1 1 0 1.3.2 2.5.6 3.6.1.3 0 .7-.2 1z"/></svg>123 456 7890</div>
  <div class="info" style="top:229px;display:flex;gap:8px;align-items:center">
    <svg width="13" height="10" viewBox="0 0 24 18"><rect width="24" height="18" rx="2" fill="#fff"/><path d="M1 2l11 8 11-8" stroke="#333" stroke-width="2" fill="none"/></svg>info@ironsidetraininghub.com</div>

  <h6 style="left:565px;width:123px">Quick <span>Contact</span></h6>
  <div class="field" style="top:76px;height:26px">Name</div>
  <div class="field" style="top:111px;height:26px">Email</div>
  <div class="field" style="top:146px;height:55px">Message</div>
  <a class="btn" href="#">Read More</a>
</footer>
<div class="abs footer-brand"><span class="mark"></span>Ironside Training Hub</div>

<div class="abs copyright">© 2017 Ironside Training Hub. All Rights Reserved.</div>

</body>
</html>
```